Menu board for car wash

I need to have a menu board designed for my car wash. I would like for it to replicate the attached graphics of other menu boards other car washes are using. The menu board will be printed locally and be cut out with a router. I want the menu board to clearly show what they are buying and promote buying the top wash package. I also want "the Fullset" package to show that you can buy a monthly plan for $23.95 and receive this wash unlimited times per month. I have attached my menu that i have now (Hendleybrightmenu). I would like for this new menu to have the same wording as the previous menu for the wash packages. The only addition is a new wash package "Summit Glow" which is now the top wash package. The new menu i would like to have going vertical and I would like my logo on the top. This menu would be 8' high and 4'wide.

Target Market(s)

Looking to have this menu be attractive and inviting. The top package should stand out the most and the lowest package should barely be noticeable ( basic wash)
I am targeting customer from the ages of 16-65 years old.

Industry/Entity Type

Automotive

Font styles to use
Serif
Sans Serif
Decorative
Other font styles liked:
• any font that flows with the design

Colors

Designer to choose colors to be used in the design.

Requirements
Must have
• This menu will be die cut out. It must fit in a 8' x 4' vertical art board.
• The wash packages will need to go from top to bottom
• They should be listed as follows
• Summit Glow $18
• The Fullset $13 ( also add Unlimited for $23.95)
• Deluxe $10
• Basic $8
• I would like to have an extras section also added just like my original menu. This can be at the bottom of the menu If you have any cool graphics that go with my theme or washes please feel free.
• The new Summit Glow wash will have the following included:
• Presoak
• Bug Treatment
• wheel cleaner
• Undercarriage wash
• Triple Foam Polish
• Clear Coat Protectant
• Hot Wax Treatment ( you can use graphic that is on my old menu for this item)
• Tire Shine ( You can use the Silk Comet logo)
• Hand Towel Dried
Nice to have
• Incorporate my business hours also on the menu
• the hours are:
• Monday-Saturday 8:00 Am-6:00 Pm
• Sunday 8:00 Am-5:00 Pm
• Weather may effect these hours
Should not have
• Text should be clearly visable so anyone car read it easily

```html
<!DOCTYPE html>
<html lang="en">
<head>
<meta charset="utf-8">
<title>Hendley Bright Car Wash – Menu Board</title>
<link href="https://fonts.googleapis.com/css2?family=Oswald:wght@600;700&family=Bungee&display=swap" rel="stylesheet">
<style>
  :root{
    --red:#d9141b;
    --red-dark:#8e0a0e;
    --yellow:#f7d312;
    --gold:#f2c21c;
    --white:#ffffff;
    --ink:#111111;
    --navy:#1f2f86;
  }
  *{box-sizing:border-box;margin:0;padding:0}
  html,body{width:1200px;height:1200px;overflow:hidden;background:#fff}
  body{position:relative;font-family:"Oswald",sans-serif}

  .board{position:absolute;top:77px;width:514px;height:1045px}
  .board--dark{left:64px;--panel-top:#2f56b8;--panel-bot:#1c3791;--edge:#3d5cc4;--frame:#2b3a9c;--chip:#1f3590}
  .board--light{left:620px;--panel-top:#35b0e8;--panel-bot:#1f93d4;--edge:#55c6f0;--frame:#2ea8e0;--chip:#58c8f2}

  .masthead{position:absolute;left:13px;top:0;width:491px;height:183px;background:var(--frame);border-radius:40px 40px 70px 70px;padding:9px}
  .masthead__inner{width:100%;height:100%;background:var(--yellow);border:7px solid var(--red);border-radius:32px 32px 60px 60px;display:flex;flex-direction:column;align-items:center;justify-content:center;line-height:.95}
  .masthead__name{font-family:"Oswald",sans-serif;font-weight:700;color:var(--red);font-size:40px;letter-spacing:1px}
  .masthead__kind{font-family:"Oswald",sans-serif;font-weight:700;color:var(--red);font-size:64px;text-transform:uppercase}

  .tier{position:absolute;left:0;width:514px;background:linear-gradient(var(--panel-top),var(--panel-bot));border:3px solid var(--edge);border-radius:18px;box-shadow:inset 0 0 0 2px rgba(0,0,0,.15)}
  .tier--summit{top:186px;height:187px}
  .tier--fullset{top:376px;height:159px}
  .tier--deluxe{top:538px;height:142px}
  .tier--basic{top:683px;height:114px}
  .tier--extras{top:801px;height:158px}

  .tier__title{position:absolute;left:0;right:0;text-align:center;font-family:"Bungee",sans-serif;color:var(--red);text-shadow:2px 2px 0 var(--red-dark),3px 3px 0 rgba(0,0,0,.35);line-height:1}
  .tier__title--extras{color:#bfe8ff;text-shadow:2px 2px 0 var(--navy)}

  .item{position:absolute;color:var(--white);font-weight:600;font-size:14px;text-transform:uppercase;white-space:nowrap;line-height:1;text-shadow:1px 1px 0 rgba(0,0,0,.4)}
  .item::before{content:"★";color:var(--gold);margin-right:6px}
  .item--plain::before{content:none}

  .price{position:absolute;background:var(--yellow);border-radius:50%;box-shadow:3px 4px 0 #111;display:flex;align-items:center;justify-content:center;font-family:"Bungee",sans-serif;color:var(--red);text-shadow:2px 2px 0 var(--red-dark)}

  .art{position:absolute;border-radius:50%}
  .art--crown{background:radial-gradient(circle at 50% 60%,#ffe27a,#d99a12)}
  .art--pots{background:radial-gradient(circle at 50% 40%,#f4c631 0 35%,#2a2a2a 36%);border-radius:45%}
  .art--gems{background:linear-gradient(135deg,#cfe6ff,#3d78e0);border-radius:40%}
  .art--coins{background:radial-gradient(circle,#f9d54a,#d49a10);border-radius:20px}

  .badge{position:absolute;display:flex;align-items:center;justify-content:center;font-weight:700;font-size:11px;text-transform:uppercase;white-space:nowrap;line-height:1}
  .badge--glaze{background:var(--yellow);color:var(--red);border-radius:4px}
  .badge--comet{background:#d8d8d8;color:var(--red);border-radius:50%}
  .badge--drop{background:var(--yellow);color:var(--navy);border-radius:2px;font-size:13px}

  .unlimited{position:absolute;left:54px;top:123px;width:228px;height:24px;background:var(--red);border-radius:12px;color:var(--white);font-weight:700;font-size:13px;display:flex;align-items:center;justify-content:center;gap:6px}
  .unlimited__amt{color:var(--yellow);font-size:17px}
  .unlimited__amt sup{font-size:10px}

  .star{position:absolute;color:var(--gold);font-size:40px;line-height:1;text-shadow:1px 1px 0 #8a6a00}

  .extra{position:absolute;top:44px;width:110px;margin-left:-55px;display:flex;flex-direction:column;align-items:center;justify-content:flex-end;height:60px;color:var(--white);font-weight:700;font-size:14px;text-transform:uppercase;text-align:center;line-height:1.05;white-space:nowrap}
  .extra .badge{position:static;margin-bottom:4px}
  .extra__chip{background:var(--chip);border-radius:50%;padding:4px 10px}
  .extra__bar{position:absolute;left:22px;top:112px;width:462px;height:34px;background:var(--white);border-radius:12px}
  .extra__price{position:absolute;top:116px;width:60px;margin-left:-30px;text-align:center;font-family:"Bungee",sans-serif;color:var(--red);font-size:22px;line-height:1.2;text-shadow:1px 1px 0 var(--red-dark)}

  .hours{position:absolute;left:0;top:962px;width:514px;height:83px;background:var(--frame);border-radius:18px;padding:5px}
  .hours__inner{width:100%;height:100%;background:var(--yellow);border:5px solid var(--red);border-radius:14px;position:relative}
  .hours__label{position:absolute;left:34px;top:14px;font-family:"Bungee",sans-serif;font-size:30px;color:var(--red);text-shadow:2px 2px 0 var(--red-dark)}
  .hours__times{position:absolute;left:155px;right:10px;top:8px;text-align:center;color:var(--ink);font-weight:700;font-size:20px;text-transform:uppercase}
  .hours__note{position:absolute;left:155px;right:10px;top:40px;text-align:center;color:var(--ink);font-weight:600;font-size:10px;text-transform:uppercase}
</style>
</head>
<body>

<section class="board board--dark">
  <header class="masthead"><div class="masthead__inner"><span class="masthead__name">Hendley Bright</span><span class="masthead__kind">Car Wash</span></div></header>

  <article class="tier tier--summit">
    <div class="art art--crown" role="img" aria-label="Gold crown illustration" style="left:6px;top:6px;width:62px;height:50px"></div>
    <div class="art art--crown" role="img" aria-label="Gold crown illustration" style="left:444px;top:6px;width:62px;height:50px"></div>
    <h2 class="tier__title" style="top:20px;font-size:32px">Summit Glow</h2>
    <span class="item" style="left:18px;top:73px">Presoak</span>
    <span class="item" style="left:18px;top:97px">Bug Treatment</span>
    <span class="item" style="left:18px;top:121px">Wheel Cleaner</span>
    <span class="item" style="left:18px;top:145px">Undercarriage Wash</span>
    <span class="item" style="left:164px;top:73px">Triple Foam Polish</span>
    <span class="item" style="left:164px;top:97px">Clear Coat Protectant</span>
    <span class="item" style="left:164px;top:121px">Hand Towel Dried</span>
    <span class="badge badge--glaze" style="left:382px;top:76px;width:88px;height:14px">Glaze Shine</span>
    <span class="item" style="left:349px;top:96px">Hot Wax Treatment</span>
    <span class="badge badge--comet" style="left:312px;top:122px;width:68px;height:24px">Silk Comet</span>
    <span class="item" style="left:308px;top:154px">Tire Shine</span>
    <div class="price" style="left:410px;top:116px;width:90px;height:66px;font-size:36px">$18</div>
  </article>

  <article class="tier tier--fullset">
    <div class="art art--pots" role="img" aria-label="Pots of gold coins illustration" style="left:26px;top:-5px;width:102px;height:62px"></div>
    <h2 class="tier__title" style="top:18px;font-size:30px">The Fullset</h2>
    <span class="badge badge--drop" style="left:398px;top:31px;width:74px;height:18px">ClearDrop</span>
    <span class="item" style="left:18px;top:58px">Presoak</span>
    <span class="item" style="left:18px;top:79px">Wheel Cleaner</span>
    <span class="item" style="left:18px;top:101px">Undercarriage Wash</span>
    <span class="item" style="left:192px;top:58px">Triple Foam Polish</span>
    <span class="item" style="left:192px;top:79px">Clear Coat Protectant</span>
    <span class="item" style="left:192px;top:101px">Hand Towel Dried</span>
    <span class="item" style="left:360px;top:57px;font-size:13px">Complete Surface</span>
    <span class="item item--plain" style="left:378px;top:70px;font-size:13px">Protectant</span>
    <span class="unlimited">UNLIMITED <span class="unlimited__amt">$23<sup>95</sup></span> / MONTH</span>
    <span class="badge badge--comet" style="left:348px;top:96px;width:68px;height:24px">Silk Comet</span>
    <span class="item" style="left:344px;top:127px">Tire Shine</span>
    <div class="price" style="left:434px;top:96px;width:78px;height:54px;font-size:30px">$13</div>
  </article>

  <article class="tier tier--deluxe">
    <div class="art art--gems" role="img" aria-label="Blue gemstones illustration" style="left:90px;top:14px;width:90px;height:42px"></div>
    <div class="art art--gems" role="img" aria-label="Blue gemstones illustration" style="left:354px;top:14px;width:92px;height:42px"></div>
    <h2 class="tier__title" style="top:16px;font-size:28px">Deluxe</h2>
    <span class="item" style="left:28px;top:63px">Presoak</span>
    <span class="item" style="left:28px;top:84px">Wheel Cleaner</span>
    <span class="item" style="left:28px;top:106px">Undercarriage Wash</span>
    <span class="item" style="left:200px;top:61px">Triple Foam Polish</span>
    <span class="item" style="left:200px;top:83px">Clear Coat Protectant</span>
    <span class="item" style="left:200px;top:103px">Hand Towel Dried</span>
    <div class="price" style="left:422px;top:70px;width:78px;height:54px;font-size:28px">$10</div>
  </article>

  <article class="tier tier--basic">
    <div class="art art--coins" role="img" aria-label="Row of gold coins illustration" style="left:62px;top:22px;width:124px;height:26px"></div>
    <div class="art art--coins" role="img" aria-label="Row of gold coins illustration" style="left:340px;top:22px;width:124px;height:26px"></div>
    <h2 class="tier__title" style="top:18px;font-size:28px">Basic</h2>
    <span class="item" style="left:54px;top:75px">Presoak</span>
    <span class="item" style="left:166px;top:75px">Wash</span>
    <span class="item" style="left:256px;top:75px">Dry</span>
    <div class="price" style="left:370px;top:56px;width:67px;height:44px;font-size:24px">$8</div>
  </article>

  <article class="tier tier--extras">
    <span class="star" style="left:136px;top:12px">★</span>
    <span class="star" style="left:350px;top:12px">★</span>
    <h2 class="tier__title tier__title--extras" style="top:16px;font-size:30px">Extras</h2>
    <div class="extra" style="left:62px"><span class="badge badge--glaze" style="width:86px;height:14px">Glaze Shine</span>Treatment</div>
    <div class="extra" style="left:168px"><span class="badge badge--comet" style="width:68px;height:22px">Silk Comet</span>Tire Dressing</div>
    <div class="extra" style="left:272px"><span class="badge badge--drop" style="width:70px;height:18px">ClearDrop</span>Treatment</div>
    <div class="extra" style="left:354px"><span class="extra__chip">Wheel<br>Cleaner</span></div>
    <div class="extra" style="left:442px"><span class="extra__chip">Undercarriage<br>Wash</span></div>
    <div class="extra__bar"></div>
    <span class="extra__price" style="left:62px">$8</span>
    <span class="extra__price" style="left:168px">$2</span>
    <span class="extra__price" style="left:272px">$2</span>
    <span class="extra__price" style="left:354px">$2</span>
    <span class="extra__price" style="left:442px">$1</span>
  </article>

  <footer class="hours"><div class="hours__inner">
    <span class="hours__label">Open:</span>
    <span class="hours__times">Mon-Sat 8am-6pm • Sun 8am-5pm</span>
    <span class="hours__note">(Weather may effect these hours.)</span>
  </div></footer>
</section>

<section class="board board--light">
  <header class="masthead"><div class="masthead__inner"><span class="masthead__name">Hendley Bright</span><span class="masthead__kind">Car Wash</span></div></header>

  <article class="tier tier--summit">
    <div class="art art--crown" role="img" aria-label="Gold crown illustration" style="left:6px;top:6px;width:62px;height:50px"></div>
    <div class="art art--crown" role="img" aria-label="Gold crown illustration" style="left:444px;top:6px;width:62px;height:50px"></div>
    <h2 class="tier__title" style="top:20px;font-size:32px">Summit Glow</h2>
    <span class="item" style="left:18px;top:73px">Presoak</span>
    <span class="item" style="left:18px;top:97px">Bug Treatment</span>
    <span class="item" style="left:18px;top:121px">Wheel Cleaner</span>
    <span class="item" style="left:18px;top:145px">Undercarriage Wash</span>
    <span class="item" style="left:164px;top:73px">Triple Foam Polish</span>
    <span class="item" style="left:164px;top:97px">Clear Coat Protectant</span>
    <span class="item" style="left:164px;top:121px">Hand Towel Dried</span>
    <span class="badge badge--glaze" style="left:382px;top:76px;width:88px;height:14px">Glaze Shine</span>
    <span class="item" style="left:349px;top:96px">Hot Wax Treatment</span>
    <span class="badge badge--comet" style="left:312px;top:122px;width:68px;height:24px">Silk Comet</span>
    <span class="item" style="left:308px;top:154px">Tire Shine</span>
    <div class="price" style="left:410px;top:116px;width:90px;height:66px;font-size:36px">$18</div>
  </article>

  <article class="tier tier--fullset">
    <div class="art art--pots" role="img" aria-label="Pots of gold coins illustration" style="left:26px;top:-5px;width:102px;height:62px"></div>
    <h2 class="tier__title" style="top:18px;font-size:30px">The Fullset</h2>
    <span class="badge badge--drop" style="left:398px;top:31px;width:74px;height:18px">ClearDrop</span>
    <span class="item" style="left:18px;top:58px">Presoak</span>
    <span class="item" style="left:18px;top:79px">Wheel Cleaner</span>
    <span class="item" style="left:18px;top:101px">Undercarriage Wash</span>
    <span class="item" style="left:192px;top:58px">Triple Foam Polish</span>
    <span class="item" style="left:192px;top:79px">Clear Coat Protectant</span>
    <span class="item" style="left:192px;top:101px">Hand Towel Dried</span>
    <span class="item" style="left:360px;top:57px;font-size:13px">Complete Surface</span>
    <span class="item item--plain" style="left:378px;top:70px;font-size:13px">Protectant</span>
    <span class="unlimited">UNLIMITED <span class="unlimited__amt">$23<sup>95</sup></span> / MONTH</span>
    <span class="badge badge--comet" style="left:348px;top:96px;width:68px;height:24px">Silk Comet</span>
    <span class="item" style="left:344px;top:127px">Tire Shine</span>
    <div class="price" style="left:434px;top:96px;width:78px;height:54px;font-size:30px">$13</div>
  </article>

  <article class="tier tier--deluxe">
    <div class="art art--gems" role="img" aria-label="Blue gemstones illustration" style="left:90px;top:14px;width:90px;height:42px"></div>
    <div class="art art--gems" role="img" aria-label="Blue gemstones illustration" style="left:354px;top:14px;width:92px;height:42px"></div>
    <h2 class="tier__title" style="top:16px;font-size:28px">Deluxe</h2>
    <span class="item" style="left:28px;top:63px">Presoak</span>
    <span class="item" style="left:28px;top:84px">Wheel Cleaner</span>
    <span class="item" style="left:28px;top:106px">Undercarriage Wash</span>
    <span class="item" style="left:200px;top:61px">Triple Foam Polish</span>
    <span class="item" style="left:200px;top:83px">Clear Coat Protectant</span>
    <span class="item" style="left:200px;top:103px">Hand Towel Dried</span>
    <div class="price" style="left:422px;top:70px;width:78px;height:54px;font-size:28px">$10</div>
  </article>

  <article class="tier tier--basic">
    <div class="art art--coins" role="img" aria-label="Row of gold coins illustration" style="left:62px;top:22px;width:124px;height:26px"></div>
    <div class="art art--coins" role="img" aria-label="Row of gold coins illustration" style="left:340px;top:22px;width:124px;height:26px"></div>
    <h2 class="tier__title" style="top:18px;font-size:28px">Basic</h2>
    <span class="item" style="left:54px;top:75px">Presoak</span>
    <span class="item" style="left:166px;top:75px">Wash</span>
    <span class="item" style="left:256px;top:75px">Dry</span>
    <div class="price" style="left:370px;top:56px;width:67px;height:44px;font-size:24px">$8</div>
  </article>

  <article class="tier tier--extras">
    <span class="star" style="left:136px;top:12px">★</span>
    <span class="star" style="left:350px;top:12px">★</span>
    <h2 class="tier__title tier__title--extras" style="top:16px;font-size:30px">Extras</h2>
    <div class="extra" style="left:62px"><span class="badge badge--glaze" style="width:86px;height:14px">Glaze Shine</span>Treatment</div>
    <div class="extra" style="left:168px"><span class="badge badge--comet" style="width:68px;height:22px">Silk Comet</span>Tire Dressing</div>
    <div class="extra" style="left:272px"><span class="badge badge--drop" style="width:70px;height:18px">ClearDrop</span>Treatment</div>
    <div class="extra" style="left:354px"><span class="extra__chip">Wheel<br>Cleaner</span></div>
    <div class="extra" style="left:442px"><span class="extra__chip">Undercarriage<br>Wash</span></div>
    <div class="extra__bar"></div>
    <span class="extra__price" style="left:62px">$8</span>
    <span class="extra__price" style="left:168px">$2</span>
    <span class="extra__price" style="left:272px">$2</span>
    <span class="extra__price" style="left:354px">$2</span>
    <span class="extra__price" style="left:442px">$1</span>
  </article>

  <footer class="hours"><div class="hours__inner">
    <span class="hours__label">Open:</span>
    <span class="hours__times">Mon-Sat 8am-6pm • Sun 8am-5pm</span>
    <span class="hours__note">(Weather may effect these hours.)</span>
  </div></footer>
</section>

</body>
</html>
```